Merrivale construction website for a high end luxury custom home builder

I need a website designed for a high end luxury custom home builder. I would like the website to host a number activities. A blog/vlog on the page where I can post about the projects being built how to's what to look out for during the build, A designated testimonial page but also having testimonials posted on the other pages like the gallery linked to the photos of the completed projects. a gallery page, an about us page, services page that demonstrate what we do and what we are capable of, and hopefully when I start winning awards, and awards page.
Home page
about us page
services page
gallery
testimonial
awards page but I my need to add that later.
I already have the domain name for the website. www.merrivaleconstruction.com.au
I recently completed a sketch hive page for my logo and will post the logo documents below.

Target Market(s)

I'd like to target professions with cash enough to build a house. I would like peolpe to understand that they are buy a price when they are getting quote to build there house. It seems like people just look for the cheapest price and end up with an inferior product. Where as people need to understand that a builder with the high price ( not astronomically higher 15-20% higher) are the ones with correct systems in place, a bide by correct OHS and use proper and correct product. If that can be conveyed through the website somehow, without saying it directly, it would be awesome.

Font styles to use
Sans Serif

Requirements
Must have
• I would like the testimonials to have a designated page (mentioned in the brief) but I would like the testimonials to be linked to the gallery page and when the picture are open of completed job the relevant testimonials would pop up near the pictures.

Nice to have
• I would like peolpe to understand that they are buy a price when they are getting quote to build there house. It seems like people just look for the cheapest price and end up with an inferior product. Where as people need to understand that a builder with the high price ( not astronomically higher 15-20% higher) are the ones with correct systems in place, a bide by correct OHS and use proper and correct product. If that can be conveyed through the website somehow, without saying it directly, it would be awesome.

```html
<!DOCTYPE html>
<html lang="en">
<head>
<meta charset="utf-8">
<title>Merrivale Construction</title>
<link href="https://fonts.googleapis.com/css2?family=Oswald:wght@400;500&family=Roboto:ital,wght@0,400;0,500;0,700;1,400&display=swap" rel="stylesheet">
<style>
:root{
  --navy:#0d131d;
  --ink:#1e2330;
  --text:#444a55;
  --muted:#8a909a;
  --accent:#6b8fc2;
  --red:#d9363e;
  --line:#e6e8ec;
  --footer:#232a3b;
  --white:#fff;
}
*{box-sizing:border-box;margin:0;padding:0}
html,body{width:1200px;height:2732px;overflow:hidden;background:var(--white)}
body{position:relative;font-family:'Roboto',sans-serif;color:var(--text);font-size:7px}
.abs{position:absolute}
.head{font-family:'Oswald',sans-serif;font-weight:400;text-transform:uppercase;color:var(--ink);line-height:1.15}
.head .accent{color:var(--accent)}
.rule{display:flex;gap:3px;margin-top:8px}
.rule i{display:block;height:2px;background:var(--red);width:16px}
.rule i+i{width:6px;background:var(--ink)}

/* nav */
.topbar{left:142px;top:0;width:917px;height:25px;background:var(--navy);display:flex;align-items:center}
.brand{width:153px;height:25px;background:var(--white);display:flex;align-items:center;padding-left:48px;gap:4px}
.brand .mark{width:12px;height:12px;background:var(--accent);border-radius:50%}
.brand span{font-family:'Oswald',sans-serif;font-size:9px;color:var(--accent);text-transform:uppercase;font-weight:500}
.nav{display:flex;gap:14px;margin-left:20px;color:#fff;font-size:6px}
.nav-right{margin-left:auto;display:flex;gap:18px;color:#fff;font-size:6px;padding-right:50px}

/* hero */
.hero{left:142px;top:25px;width:917px;height:404px;background:linear-gradient(120deg,#2b3644 0%,#3d4a57 35%,#6b5a4c 60%,#4a4e55 100%)}
.hero-card{left:387px;top:97px;width:203px;height:261px;background:rgba(10,13,18,.93);padding:32px 36px}
.hero-card .bar{width:52px;height:1px;background:var(--accent);margin-bottom:20px}
.hero-card h1{font-family:'Oswald',sans-serif;font-weight:400;font-size:23px;line-height:30px;color:#fff;text-transform:uppercase}
.hero-card p{color:#fff;font-size:6px;line-height:11px;margin-top:22px}
.btn-ghost{display:inline-block;margin-top:18px;border:1px solid #fff;color:#fff;font-size:5px;padding:6px 20px}

/* about */
.years{left:393px;top:497px;width:166px;height:203px;background:linear-gradient(135deg,#5a7aa6,#8b3a4a)}
.years .inner{position:absolute;left:7px;top:7px;width:152px;height:189px;background:#fff;text-align:center}
.years .num{font-family:'Oswald',sans-serif;font-weight:500;font-size:96px;line-height:1;margin-top:38px;color:#3b4b63;letter-spacing:-4px}
.years .cap{font-size:11px;color:var(--muted);margin-top:2px}
.about{left:596px;top:500px;width:175px}
.about .head{font-size:18px}
.about p{font-size:5.5px;line-height:11px;margin-top:16px}
.checks{list-style:none;margin-top:10px}
.checks li{display:flex;align-items:center;gap:5px;font-size:5.5px;color:var(--accent);line-height:11px}
.checks li b{width:7px;height:7px;background:var(--red);border-radius:1px;display:block}
.stats{display:flex;gap:34px;margin-top:14px;border-top:1px solid var(--line);padding-top:8px;width:160px}
.stats div{display:flex;align-items:center;gap:6px}
.stats strong{font-family:'Oswald',sans-serif;font-weight:500;color:var(--accent);font-size:11px}
.stats span{font-size:5px}

/* facilities */
.facility-band{left:142px;top:767px;width:917px;height:173px;background:linear-gradient(90deg,#1b1f24,#3a3124 30%,#2c2820 60%,#1c2128)}
.facility-title{left:142px;top:832px;width:917px;text-align:center;color:#fff;font-size:18px}
.facilities{left:393px;top:891px;width:415px;height:163px;display:flex;background:#fff;box-shadow:0 1px 3px rgba(0,0,0,.08)}
.facility{flex:1;border-right:1px solid var(--line);text-align:center;padding-top:22px}
.facility:last-child{border-right:0}
.facility h3{font-family:'Oswald',sans-serif;font-weight:400;font-size:7px;color:var(--ink);margin-top:16px}
.facility p{font-size:5px;line-height:9.5px;color:var(--text);margin:8px 14px 0}
.facility a{display:block;font-size:4.5px;font-weight:700;color:var(--ink);margin-top:12px}

/* certificates */
.cert-head{left:393px;top:1145px}
.cert-head .head{font-size:18px}
.cert{top:1122px;width:68px;height:95px;box-shadow:0 1px 3px rgba(0,0,0,.2)}
.cert.c1{left:537px;background:#f6ece0;border:3px solid #d7b88f}
.cert.c2{left:637px;background:linear-gradient(#f4f4f6 70%,#243a6e 70%);border:3px solid #243a6e}
.cert.c3{left:737px;background:#faf8f2;border:3px solid #c9a040}

/* properties */
.prop{top:1286px;width:294px;height:286px;color:#fff}
.prop .label{position:absolute;left:11px;bottom:12px}
.prop .price{font-family:'Oswald',sans-serif;font-size:9px}
.prop .name{font-size:7px;margin-top:7px}
.prop .meta{font-size:6.5px;margin-top:10px;word-spacing:4px}
.p1{left:142px;background:linear-gradient(160deg,#d9d5cf,#8c5647 55%,#3b3330)}
.p2{left:448px;background:linear-gradient(180deg,#3c78c6 0%,#7aa0c9 40%,#4d5046 70%,#2b3a2e)}
.p3{left:753px;background:linear-gradient(180deg,#1c46a0 0%,#4a6fb8 45%,#e8ecef 60%,#3b4040)}
.arrow{top:1418px;width:19px;height:19px;border:1px solid #fff;border-radius:50%;display:flex;align-items:center;justify-content:center}

/* testimonial */
.avatar{left:575px;top:1640px;width:50px;height:50px;border-radius:50%;background:linear-gradient(#c9ccd2,#7b8592)}
.quote-mark{left:606px;top:1676px;color:var(--red);font-family:'Oswald',sans-serif;font-size:16px;line-height:1}
.testi{left:420px;top:1694px;width:360px;text-align:center}
.testi .name{font-family:'Oswald',sans-serif;font-size:7px;color:var(--ink)}
.testi .role{font-size:4.5px;color:var(--muted);margin-top:2px}
.testi blockquote{font-style:italic;font-size:8px;line-height:15px;margin-top:20px}
.dots{display:flex;gap:4px;justify-content:center;margin-top:17px}
.dots i{width:3px;height:3px;border-radius:50%;background:#ccc}
.dots i:last-child{background:var(--ink)}

/* quotation */
.quote-left{left:393px;top:1865px;width:207px;height:204px;border-bottom:1px solid var(--line)}
.quote-left .head{position:absolute;left:34px;top:86px;font-size:17px}
.quote-left .sub{position:absolute;left:34px;top:128px;font-size:5px}
.quote-left .btn{position:absolute;left:34px;top:154px;width:68px;height:19px;border:1px solid var(--accent);color:var(--accent);font-size:4.5px;display:flex;align-items:center;justify-content:center}
.quote-photo{left:600px;top:1865px;width:459px;height:249px;background:linear-gradient(100deg,#dfe6ec 0%,#d4cfc7 45%,#b9a997 65%,#eef0f1 80%,#cfd3d6)}
.call{left:600px;top:1911px;width:208px;height:157px;background:rgba(255,255,255,.86);padding:66px 0 0 20px;display:flex;gap:14px}
.call .ring{width:26px;height:26px;border-radius:50%;border:1px solid #e9c8c8;display:flex;align-items:center;justify-content:center;background:#fff}
.call small{font-size:5px;color:var(--ink);display:block}
.call strong{font-family:'Oswald',sans-serif;font-weight:500;font-size:14px;color:var(--accent);display:block;margin-top:4px}

/* news */
.news-title{left:142px;top:2184px;width:917px;text-align:center;font-size:18px}
.news-rule{left:586px;top:2208px}
.news{top:2242px;width:202px;height:201px}
.news .img{position:absolute;left:0;top:0;width:202px;height:134px}
.news .date{position:absolute;left:0;top:144px;width:29px;height:32px;background:var(--accent);color:#fff;text-align:center;font-family:'Oswald',sans-serif;font-size:9px;padding-top:5px;line-height:1}
.news .date small{display:block;font-size:4.5px;margin-top:1px}
.news .body{position:absolute;left:42px;top:128px;width:160px;height:73px;background:#fff;padding:10px 15px;box-shadow:0 1px 3px rgba(0,0,0,.06)}
.news .cat{font-size:4px;color:var(--muted)}
.news h4{font-family:'Roboto',sans-serif;font-weight:500;font-size:8px;line-height:13px;color:var(--ink);margin-top:4px}
.news .more{font-size:4px;font-weight:700;color:var(--ink);margin-top:10px}
.n1{left:393px}.n2{left:607px}
.n1 .img{background:linear-gradient(180deg,#e9e9e7,#c9c3be)}
.n2 .img{background:linear-gradient(135deg,#dbe9f2,#4c9a3a 50%,#1c5a2a)}

/* footer */
.footer{left:142px;top:2511px;width:917px;height:221px;background:var(--footer);color:#c9ceda}
.f-brand{position:absolute;left:19px;top:98px;display:flex;align-items:center;gap:10px}
.f-brand .mark{width:40px;height:40px;border-radius:50%;background:#2d6fc0}
.f-brand span{font-family:'Oswald',sans-serif;font-size:28px;color:#2d6fc0;text-transform:uppercase;letter-spacing:1px}
.f-col{position:absolute;top:59px;width:96px}
.f-col h5{font-family:'Oswald',sans-serif;font-weight:500;font-size:6px;color:#fff;text-transform:uppercase}
.f-col p,.f-col li{font-size:4.8px;line-height:10px;margin-top:4px;list-style:none}
.f-col li{margin-top:0}
.f-col ul{margin-top:4px}
.news-form{display:flex;margin-top:16px;width:96px;height:14px}
.news-form span{flex:1;background:#fff;font-size:4px;color:#999;padding:4px 6px}
.news-form b{width:22px;background:var(--accent);display:flex;align-items:center;justify-content:center}
.copy{position:absolute;left:251px;top:203px;font-size:4.8px}
.social{position:absolute;left:604px;top:203px;display:flex;gap:14px}
.social i{width:5px;height:5px;border-radius:50%;background:#8891a4;display:block}
</style>
</head>
<body>

<header class="abs topbar">
  <div class="brand"><b class="mark"></b><span>Merrivale</span></div>
  <nav class="nav"><span>Home</span><span>About Us</span><span>Services</span><span>Gallery</span><span>Testimonial</span></nav>
  <div class="nav-right"><span>Login</span><span>Call us +001 480 216</span></div>
</header>

<section class="abs hero" role="img" aria-label="Photo of a modern interior with floating timber staircase and glass balustrade"></section>
<div class="abs hero-card">
  <div class="bar"></div>
  <h1>We create<br>your deam<br>appartment</h1>
  <p>Lorem ipsum dolor sit amet, consectetur adipilit, sed do eiusmod tempor incididunt ut labore et dolore magna aliqua Quis.</p>
  <span class="btn-ghost">View Project</span>
</div>

<div class="abs years"><div class="inner"><div class="num">10</div><div class="cap">Years of Exprince</div></div></div>
<section class="abs about">
  <h2 class="head">We are Merrivale<br><span class="accent">unique company</span></h2>
  <div class="rule"><i></i><i></i></div>
  <p>Lorem ipsum dolor sit amet, consectetur adipisicing elit, sed do eiusmod tempor incididunt ut labore et dolore magna aliqua. Ut enim ad minim veniam, quis nostrud.</p>
  <ul class="checks">
    <li><b></b>Lorem ipsum dolor sit amet</li>
    <li><b></b>Consectetur adipisicing elit, sed do</li>
    <li><b></b>Eiusmod tempor incididunt ut labore</li>
    <li><b></b>Ad minim veniam, quis nostrud</li>
  </ul>
  <div class="stats"><div><strong>120</strong><span>Buildings</span></div><div><strong>500+</strong><span>Clients</span></div></div>
</section>

<section class="abs facility-band" role="img" aria-label="Night photo of a lit glass-walled living room"></section>
<h2 class="abs head facility-title" style="color:#fff">Our facilities</h2>
<div class="abs facilities">
  <div class="facility">
    <svg width="28" height="28" viewBox="0 0 28 28" fill="none" stroke="#1e2330" stroke-width="1.2"><rect x="4" y="8" width="18" height="16"/><path d="M10 20l13-13 3 3-13 13h-3z"/><path d="M6 12h6M6 16h4"/></svg>
    <h3>PLANNING STAGE</h3>
    <p>Lorem ipsum dolor sit amet, consectetur adipisicing elit, sed do eiusmod tempor incididunt ut labore et dolore magna.</p>
    <a>Learn more</a>
  </div>
  <div class="facility">
    <svg width="28" height="28" viewBox="0 0 28 28" fill="none" stroke="#1e2330" stroke-width="1.2"><rect x="7" y="3" width="14" height="22"/><rect x="3" y="11" width="4" height="14"/><rect x="21" y="11" width="4" height="14"/><path d="M10 7h2M16 7h2M10 11h2M16 11h2M10 15h2M16 15h2M10 19h2M16 19h2M12 25v-3h4v3"/></svg>
    <h3>PLANNING STAGE</h3>
    <p>Lorem ipsum dolor sit amet, consectetur adipisicing elit, sed do eiusmod tempor incididunt ut labore et dolore magna.</p>
    <a>Learn more</a>
  </div>
  <div class="facility">
    <svg width="28" height="28" viewBox="0 0 28 28" fill="none" stroke="#d9363e" stroke-width="2"><path d="M5 16v-3a9 9 0 0 1 18 0v3"/><rect x="4" y="15" width="4" height="7" rx="1"/><rect x="20" y="15" width="4" height="7" rx="1"/><path d="M22 22c0 3-3 4-7 4"/></svg>
    <h3>PLANNING STAGE</h3>
    <p>Lorem ipsum dolor sit amet, consectetur adipisicing elit, sed do eiusmod tempor incididunt ut labore et dolore magna.</p>
    <a>Learn more</a>
  </div>
</div>

<div class="abs cert-head">
  <h2 class="head">Property<br><span class="accent">certificates</span></h2>
  <div class="rule"><i></i><i></i></div>
</div>
<div class="abs cert c1" role="img" aria-label="Certificate of achievement"></div>
<div class="abs cert c2" role="img" aria-label="Certificate with blue border"></div>
<div class="abs cert c3" role="img" aria-label="Certificate with gold border"></div>

<article class="abs prop p1" role="img" aria-label="Photo of a living room with a brick fireplace">
  <div class="label"><div class="price">$35,000</div><div class="name">COLORFUL LITTLE APRTMENT</div><div class="meta">2BD | 2BA | 920 SF</div></div>
</article>
<article class="abs prop p2" role="img" aria-label="Photo of a white modern house with glass walls">
  <div class="label"><div class="price">$35,000</div><div class="name">COLORFUL LITTLE APRTMENT</div><div class="meta">2BD | 2BA | 920 SF</div></div>
</article>
<article class="abs prop p3" role="img" aria-label="Photo of white apartment terraces against blue sky">
  <div class="label"><div class="price">$35,000</div><div class="name">COLORFUL LITTLE APRTMENT</div><div class="meta">2BD | 2BA | 920 SF</div></div>
</article>
<div class="abs arrow" style="left:160px"><svg width="6" height="6" viewBox="0 0 6 6" fill="none" stroke="#fff"><path d="M4 1L2 3l2 2"/></svg></div>
<div class="abs arrow" style="left:1020px"><svg width="6" height="6" viewBox="0 0 6 6" fill="none" stroke="#fff"><path d="M2 1l2 2-2 2"/></svg></div>

<div class="abs avatar" role="img" aria-label="Client portrait"></div>
<div class="abs quote-mark">&rdquo;</div>
<section class="abs testi">
  <div class="name">Darra Kell</div>
  <div class="role">Creative Director</div>
  <blockquote>"I am at an age where I just want to be fit and healthy our bodies are our responsibility! So start caring for your body and it will care for you. Eat clean it will care for you and workout hard."</blockquote>
  <div class="dots"><i></i><i></i><i></i></div>
</section>

<section class="abs quote-left">
  <h2 class="head">Get a free<br>quotation today!</h2>
  <div class="sub">Have any questions in mind?</div>
  <div class="btn">Contact Us</div>
</section>
<div class="abs quote-photo" role="img" aria-label="Photo of a contemporary white apartment facade"></div>
<div class="abs call">
  <div class="ring"><svg width="10" height="10" viewBox="0 0 10 10" fill="var(--red)"><path d="M2 1l2 2-1 1a5 5 0 0 0 3 3l1-1 2 2-1 1.5C4 9 1 6 .5 3z"/></svg></div>
  <div><small>Say Hello,</small><strong>+44 570 214 3968</strong></div>
</div>

<h2 class="abs head news-title">Our latest news</h2>
<div class="abs rule news-rule"><i></i><i></i></div>
<article class="abs news n1">
  <div class="img" role="img" aria-label="Photo of a family sitting against a white brick wall"></div>
  <div class="date">24<small>Nov</small></div>
  <div class="body"><div class="cat">| Properties</div><h4>FOOTPRINTS IN TIME: HOUSE IN KURASHIKI, JAPAN</h4><div class="more">READ MORE »</div></div>
</article>
<article class="abs news n2">
  <div class="img" role="img" aria-label="Photo of a building with green glass balconies"></div>
  <div class="date">24<small>Nov</small></div>
  <div class="body"><div class="cat">| Properties</div><h4>FOOTPRINTS IN TIME: HOUSE IN KURASHIKI, JAPAN</h4><div class="more">READ MORE »</div></div>
</article>

<footer class="abs footer">
  <div class="f-brand"><b class="mark"></b><span>Merrivale</span></div>
  <div class="f-col" style="left:251px"><h5>About us</h5><p>Heaven fruitful doesn't over lesser days appear creeping seasons so behold bearing days open</p></div>
  <div class="f-col" style="left:358px"><h5>Contact info</h5><p>Address :Your address goes here, your demo address.<br>Phone : +8800 55120734<br>hello@merrivalemail.com</p></div>
  <div class="f-col" style="left:464px"><h5>Important link</h5><ul><li>View Project</li><li>Contact Us</li><li>Testimonial</li><li>Properties</li><li>Support</li></ul></div>
  <div class="f-col" style="left:571px"><h5>Newsletter</h5><p>Heaven fruitful doesn't over lesser in days. Appear creeping seasons</p>
    <div class="news-form"><span>Enter your mail</span><b><svg width="6" height="6" viewBox="0 0 6 6" fill="#fff"><path d="M0 3l6-3-2 6-1-2z"/></svg></b></div></div>
  <div class="copy">Copyright ©2020 All rights reserved | This template is made with ♥ by Lornfield</div>
  <div class="social"><i></i><i></i><i></i><i></i></div>
</footer>

</body>
</html>
```